Company Mission & Values Poster

I'd like an A2 Portrait Poster displaying our company's Mission & Values.
See our website for our logo, fonts, mission & values.
https://talvendo.com.au/

Our Mission: Creating homes for abundant life
Values: Love, Thinking, Team, Zoe.

Some ideas to consider:
Mission as the Headline then
A logo for each of the 4 Values and the words

Target Market(s)

Myself & my team

Industry/Entity Type

Real Estate

Font styles to use
Other font styles liked:
• Company fonts as seen on our website

```html
<!DOCTYPE html>
<html lang="en">
<head>
<meta charset="utf-8">
<title>Talvendo — Mission &amp; Values</title>
<link rel="stylesheet" href="https://fonts.googleapis.com/css2?family=Gilda+Display&family=Gloock&family=Manrope:wght@300;500&display=swap">
<style>
  :root {
    --hero-top: #3a5f52;
    --hero-bottom: #2b4f42;
    --forest: #0a3630;
    --card: #17615a;
    --rule: #2f9c90;
    --paper: #f5f7f6;
    --ink-light: #ffffff;
    --ink-dark: #0a3630;
    --display: "Gloock", Georgia, serif;
    --serif: "Gilda Display", Georgia, serif;
    --sans: "Manrope", "Helvetica Neue", Arial, sans-serif;
  }
  * { margin: 0; padding: 0; box-sizing: border-box; }
  html, body { width: 849px; height: 1200px; overflow: hidden; background: var(--paper); }
  .poster { position: relative; width: 849px; height: 1200px; }

  .hero { position: absolute; inset: 0 0 auto 0; height: 392px; color: var(--ink-light); text-align: center; }
  .hero-photo { position: absolute; inset: 0; background: linear-gradient(180deg, var(--hero-top) 0%, #40665a 45%, var(--hero-bottom) 100%); }
  .hero-title { position: relative; font-family: var(--display); font-weight: 400; font-size: 69px; line-height: 68px; padding-top: 54px; letter-spacing: 0.8px; }
  .hero-intro { position: relative; font-family: var(--sans); font-weight: 500; font-size: 17.5px; line-height: 25.5px; margin-top: 48px; }

  .values { position: absolute; top: 392px; left: 0; width: 849px; height: 667px; background: var(--forest); }
  .belief { font-family: var(--serif); font-weight: 400; color: var(--ink-light); text-align: center; font-size: 32px; line-height: 37px; margin-top: 66px; letter-spacing: 0.6px; }

  .value-card { position: absolute; top: 301px; width: 182px; height: 325px; background: var(--card); border-radius: 0 0 22px 22px; color: var(--ink-light); text-align: center; }
  .value-card.love { left: 32px; }
  .value-card.thinking { left: 234px; }
  .value-card.team { left: 436px; }
  .value-card.zoe { left: 638px; }
  .value-badge { position: absolute; left: 50%; top: -60px; width: 120px; height: 120px; margin-left: -60px; border-radius: 50%; background: var(--card); border: 4.5px solid var(--forest); border-top-color: transparent; display: flex; align-items: center; justify-content: center; }
  .value-badge::before { content: ""; position: absolute; inset: -4.5px; border-radius: 50%; border: 4.5px solid var(--card); border-bottom-color: transparent; border-left-color: transparent; border-right-color: transparent; }
  .value-badge svg { width: 70px; height: 70px; position: relative; }
  .value-name { font-family: var(--serif); font-weight: 400; font-size: 35px; line-height: 1; margin-top: 76px; letter-spacing: 0.5px; }
  .value-rule { width: 148px; height: 1.5px; background: var(--rule); margin: 8px auto 12px; }
  .value-text { font-family: var(--sans); font-weight: 300; font-size: 13px; line-height: 17px; padding: 0 13px; }

  .brand-bar { position: absolute; left: 0; bottom: 0; width: 849px; height: 141px; background: var(--paper); display: flex; align-items: center; justify-content: center; gap: 16px; }
  .brand-dot { width: 34px; height: 34px; border-radius: 50%; background: var(--ink-dark); }
  .brand-name { font-family: var(--serif); font-weight: 400; font-size: 48px; color: var(--ink-dark); letter-spacing: 0.14em; line-height: 1; }
</style>
</head>
<body>
<main class="poster">
  <header class="hero">
    <div class="hero-photo" role="img" aria-label="Photograph of a modern multi-level home surrounded by lush gardens and trees, tinted deep green"></div>
    <h1 class="hero-title">Creating homes for<br>abundant life</h1>
    <p class="hero-intro">We wholeheartedly believe that home is an extraordinary place:<br>A haven where life unfolds in all its glory.<br>Where we find solace, make cherished memories with loved ones,<br>and savour the&nbsp; natural beauty that surrounds us.</p>
  </header>

  <section class="values">
    <p class="belief">We believe business can be a force for good.<br>Our values shape the way we work,<br>and how we make decisions.</p>

    <article class="value-card love">
      <div class="value-badge">
        <svg viewBox="0 0 70 70" aria-hidden="true">
          <path d="M35 52 C20 42 12 34 12 25 C12 18 17 13 23.5 13 C28.5 13 32.5 16 35 20 C37.5 16 41.5 13 46.5 13 C53 13 58 18 58 25 C58 34 50 42 35 52 Z" fill="#fff"/>
          <path d="M35 42 C27 36 23 31 23 26.5 C23 23 25.5 21 28.5 21 C31.5 21 33.5 23 35 25 C36.5 23 38.5 21 41.5 21 C44.5 21 47 23 47 26.5 C47 31 43 36 35 42 Z" fill="#17615a"/>
        </svg>
      </div>
      <h2 class="value-name">Love</h2>
      <div class="value-rule"></div>
      <p class="value-text">Our mission is founded in our love and respect for people - those we develop for, those in our teams and those in the communities we create and operate within.</p>
    </article>

    <article class="value-card thinking">
      <div class="value-badge">
        <svg viewBox="0 0 70 70" aria-hidden="true" fill="none" stroke="#fff" stroke-width="2.6" stroke-linecap="round" stroke-linejoin="round">
          <path d="M35 19 C27 19 22 25 22 31.5 C22 36.5 25 39.5 27.5 42 L28.5 47 H41.5 L42.5 42 C45 39.5 48 36.5 48 31.5 C48 25 43 19 35 19 Z"/>
          <path d="M31 47 V36 M39 47 V36 M31 36 C29 36 29 33 31 33 C33 33 33 36 31 36 M39 36 C37 36 37 33 39 33 C41 33 41 36 39 36"/>
          <path d="M29 51 H41 M30.5 55 H39.5"/>
          <path d="M35 8 V12 M18 15 L21 18 M52 15 L49 18 M11 31 H15 M55 31 H59 M18 47 L21 44 M52 47 L49 44"/>
        </svg>
      </div>
      <h2 class="value-name">Thinking</h2>
      <div class="value-rule"></div>
      <p class="value-text">We believe in the power of thinking. Our rigorous and creative processes create beautifully considered solutions for our purchasers, the communities we develop within and the environment.</p>
    </article>

    <article class="value-card team">
      <div class="value-badge">
        <svg viewBox="0 0 70 70" aria-hidden="true">
          <circle cx="35" cy="35" r="30" fill="#fff"/>
          <g fill="none" stroke="#17615a" stroke-width="3" stroke-linecap="round">
            <path d="M22 19 A20 20 0 0 1 46 16"/>
            <path d="M55 30 A20 20 0 0 1 44 53"/>
            <path d="M27 54 A20 20 0 0 1 15 34"/>
          </g>
          <circle cx="36" cy="17" r="5.5" fill="#17615a"/>
          <circle cx="20" cy="45" r="5.5" fill="#17615a"/>
          <circle cx="51" cy="42" r="5.5" fill="#17615a"/>
        </svg>
      </div>
      <h2 class="value-name">Team</h2>
      <div class="value-rule"></div>
      <p class="value-text">Property development is a team sport. We surround ourselves with the best designers and advisers. We strive to create an environment that allows them to do their best work and love doing it.</p>
    </article>

    <article class="value-card zoe">
      <div class="value-badge">
        <svg viewBox="0 0 70 70" aria-hidden="true" fill="none" stroke="#fff" stroke-width="2.4" stroke-linejoin="round">
          <path d="M2 35 H13 L19 26 L25 41 L33 6 L40 61 L45 35 H68"/>
        </svg>
      </div>
      <h2 class="value-name">Zoe</h2>
      <div class="value-rule"></div>
      <p class="value-text">Our mission is to create places for ‘Zoe’ - the Greek word for abundant life. We do this through exquisite design, quality construction and celebrating nature.</p>
    </article>
  </section>

  <footer class="brand-bar">
    <span class="brand-dot" aria-hidden="true"></span>
    <span class="brand-name">TALVENDO</span>
  </footer>
</main>
</body>
</html>
```